Ledgerwise - New design for a couple of our pages

We need a total renovation of one of our webpages. First we would like the "insight and analysis" to be redesigned- for now we think the page is ok, but we want it to be great. We want this design to

We specialize in business intelligence and business management software. We are open for removal of some of the text on the site. Generally, we want the page to reflect that we are a modern technology company. See the frontpage of the website for common colors, however, we are open for better ones. We also need the design implemented on our site. If the page becomes a success, then there is a good chance that we would like a similar design for the other pages as well.Se link for the page that we need improved:https://www.ledgerwise-demo.com/project/innsikt-og-analyse/?lang=en

Our main page also needs to be improved, here you will find our color palette, we would like more modern colors.

Sites we want to see with the new design suggestion:

Main page:
https://www.ledgerwise-demo.com/

about us:
https://www.ledgerwise-demo.com/aboutus/?lang=en

Finance and planning:
https://www.ledgerwise-demo.com/project/finance-and-planning/?lang=en

Retail:
https://www.ledgerwise-demo.com/project/retail/?lang=en

Target Market(s)

30 + / Business oriented / Desicion makers / financial officers / Educated

Industry/Entity Type

Information Technology

Number of Pages Required

5+ page

Font styles to use
Sans Serif

Requirements
Must have
• - Overall, we want the page to trigger the visitor to call us and schedule a meeting.
Nice to have
• Nice to have a sugguestion for a call to action - e.g. contact form. We are open to remove text and add another level of paiges under this one - again, open for suggestions for the content as well.
• We want similar colors to the already used greens and blue shades - but the designer may improble the color selection. Perhaps the designer can suggest a few options.

```html
<!DOCTYPE html>
<html lang="en">
<head>
<meta charset="utf-8">
<title>Ledgerwise – Insights and Analytics</title>
<link href="https://fonts.googleapis.com/css2?family=Poppins:wght@300;400;500;600;700&display=swap" rel="stylesheet">
<style>
:root{
  --stage:#ececec;
  --navy:#12104d;
  --navy-deep:#0b0a33;
  --indigo:#241f7a;
  --green:#8cc63f;
  --white:#ffffff;
  --ink:#2a2a3a;
  --muted:#8a8a9a;
  --card:#f2f4f8;
  --tile:#e9e9ee;
}
*{box-sizing:border-box;margin:0;padding:0}
html,body{width:1200px;height:1200px;overflow:hidden;background:var(--stage);font-family:'Poppins',sans-serif}
.page{position:absolute;left:469px;top:0;width:329px;height:1500px;transform:scale(.8);transform-origin:0 0;background:var(--white);overflow:hidden}
.abs{position:absolute}
.band{position:absolute;left:0;width:329px;background:var(--navy)}
.band-glow{background:radial-gradient(ellipse at 70% 40%,#2a2490 0%,var(--navy) 60%)}
.txt{font-size:2.6px;line-height:4.2px;color:var(--muted)}
.band .txt,.box .txt{color:#c9c8e6}
.h2{font-size:7px;font-weight:400;color:var(--ink);line-height:9px}
.band .h2,.box .h2{color:var(--white)}
.btn{position:absolute;height:8px;background:var(--green);color:var(--white);font-size:2.6px;line-height:8px;text-align:center;border-radius:1px}
.ph{position:absolute}
.circle-ph{border-radius:50%;background:radial-gradient(circle,#f4f4f6 55%,#e4e4ea 100%)}
.logo{font-weight:700;color:var(--white);font-size:7px}
.nav{position:absolute;left:119px;top:14px;display:flex;gap:8px;font-size:2.8px;color:#cfd0f0}
.hero-title{position:absolute;left:41px;top:58px;font-size:15px;line-height:18px;font-weight:500;color:var(--white)}
.hero-title span{color:var(--green);font-weight:400}
.expert-card{position:absolute;top:212px;width:50px;height:42px;background:var(--card);border-radius:2px;padding:7px 6px;font-size:2.3px;line-height:5px;color:var(--muted)}
.expert-card.active{background:var(--white);box-shadow:0 1px 5px rgba(0,0,0,.15);top:210px;height:46px}
.expert-card li{list-style:none}
.expert-card li::before{content:"• ";color:var(--green)}
.box{position:absolute;background:var(--navy)}
.checks{position:absolute;font-size:2.6px;line-height:7.5px;color:var(--ink)}
.checks li{list-style:none;display:flex;align-items:center;gap:3px}
.tick{width:4px;height:4px;background:var(--green);display:inline-block;border-radius:.5px;position:relative}
.tick::after{content:"";position:absolute;left:1.2px;top:.4px;width:1px;height:2px;border:solid #fff;border-width:0 .5px .5px 0;transform:rotate(45deg)}
.tile{position:absolute;width:50px;height:40px;background:var(--tile);border-radius:2px;font-size:2.2px;color:var(--ink);text-align:center}
.tile svg{position:absolute;left:19px;top:10px}
.tile span{position:absolute;left:0;right:0;top:27px}
.tile.active{background:var(--navy);color:var(--white);box-shadow:0 0 0 1.5px #c9c9d6}
.green{color:var(--green)}
</style>
</head>
<body>
<main class="page">

  <!-- Hero -->
  <section class="band band-glow" style="top:0;height:168px">
    <div class="abs logo" style="left:41px;top:11px">Ledgerwise</div>
    <nav class="nav"><span>Home</span><span>Industries ▾</span><span>Solutions ▾</span><span>Courses ▾</span><span>Customers ▾</span><span>About us ▾</span></nav>
    <svg class="abs" style="left:284px;top:13px" width="5" height="5" viewBox="0 0 10 10"><circle cx="4" cy="4" r="3" fill="none" stroke="#cfd0f0" stroke-width="1.3"/><path d="M6.5 6.5L9 9" stroke="#cfd0f0" stroke-width="1.3"/></svg>
    <h1 class="hero-title">Insights <span>and</span><br>Analytics</h1>
    <p class="abs" style="left:41px;top:101px;font-size:4.6px;color:#dcdcf2">Accurate information. Faster.</p>
    <div class="ph" role="img" aria-label="Illustration of two business people standing on a glowing platform" style="left:195px;top:40px;width:100px;height:105px;border-radius:45% 45% 50% 50%;background:radial-gradient(ellipse at 60% 70%,#3ad6c4 0%,#3b2fb0 35%,rgba(36,31,122,0) 70%)"></div>
  </section>

  <!-- Core expertise -->
  <section>
    <svg class="abs" style="left:162px;top:183px" width="5" height="6" viewBox="0 0 10 12"><path d="M5 1C1 5 1 10 5 11C9 10 9 5 5 1Z" fill="var(--green)"/></svg>
    <h2 class="abs" style="left:0;width:329px;top:193px;text-align:center;font-size:6.5px;font-weight:600;color:var(--ink)">Core Expertise</h2>
    <ul class="expert-card" style="left:77px"><li>Cognis Intelligence</li><li>Advanced Analytics</li><li>Machine Learning</li><li>Internet of Things</li></ul>
    <ul class="expert-card active" style="left:147px;width:44px;padding:7px 4px"><li>Ledgerwise BI</li><li>Pulse BI</li><li>Self-service reporting</li><li>Solution</li><li>Data catalog</li></ul>
    <ul class="expert-card" style="left:202px"><li>Reporting</li><li>Data integration</li><li>Cloud stream analytics</li><li>Data lake</li><li>Insights</li></ul>
  </section>

  <!-- More value -->
  <section class="band" style="top:270px;height:110px">
    <h2 class="abs h2" style="left:41px;top:11px">More value of your data</h2>
    <div class="abs txt" style="left:41px;top:24px;width:118px">
      <p>Ledgerwise gives you the tools you need to make better decisions that lift your company toward growth and steady results.</p>
      <p style="margin-top:3px">Ledgerwise is an expert in data warehousing, reporting and analysis, built on modern cloud platforms.</p>
      <p style="margin-top:3px">We combine deep domain knowledge with solid technical skill and practical experience.</p>
      <p style="margin-top:3px">We have the skills and tools needed to build solutions based on your needs, whether that means new systems or improving the ones you already use.</p>
    </div>
    <div class="btn" style="left:41px;top:85px;width:33px;height:9px;line-height:9px">Contact us</div>
    <div class="ph" role="img" aria-label="Video preview of a dashboard on a monitor" style="left:205px;top:29px;width:82px;height:54px;border:2px solid #8a8aa0;border-radius:2px;background:linear-gradient(160deg,#5a6b8c,#2e3a56)">
      <svg class="abs" style="left:34px;top:21px" width="10" height="8" viewBox="0 0 10 8"><rect width="10" height="8" rx="2" fill="#fff"/><path d="M4 2L7 4L4 6Z" fill="#444"/></svg>
    </div>
  </section>

  <!-- Dashboard og Reporting -->
  <section>
    <div class="ph circle-ph" role="img" aria-label="Tablet showing a colourful reporting dashboard" style="left:49px;top:405px;width:77px;height:80px"></div>
    <h2 class="abs h2" style="left:160px;top:418px">Dashboard og Reporting</h2>
    <div class="abs txt" style="left:160px;top:432px;width:122px">
      <p>With Ledgerwise reporting and dashboards you get clear insight into figures, giving your organisation fast and easy access to the key numbers it needs.</p>
      <p style="margin-top:3px">This lets users see results faster, spot trends early and act on what they see, with reports ready when they need them.</p>
      <p style="margin-top:3px;color:var(--ink)">Reporting has never been better and faster.</p>
    </div>

    <h2 class="abs h2" style="left:41px;width:120px;top:500px;text-align:right;font-weight:500">CASE STUDY:</h2>
    <p class="abs" style="left:41px;width:120px;top:511px;text-align:right;font-size:3.6px;color:var(--ink)">Dashboard for hospital antibiotic use</p>
    <div class="abs txt" style="left:46px;top:521px;width:115px;text-align:right">
      <p>We have created a solution for hospital pharmacies which gives them an overview of antibiotic use across wards and helps each unit follow usage over time.</p>
      <p style="margin-top:3px">The project is a collaboration between hospital staff and our team. The solution brings data together and lets users track consumption and changes in antibiotic use in a clear and simple way.</p>
    </div>
    <div class="btn" style="left:102px;top:575px;width:59px">→ Visit the solution here</div>
    <div class="ph circle-ph" role="img" aria-label="Laptop showing a hospital usage dashboard" style="left:199px;top:500px;width:77px;height:85px"></div>

    <h2 class="abs h2" style="left:41px;top:599px;font-size:6px">Datawarehouse</h2>
    <div class="abs txt" style="left:41px;top:614px;width:105px">
      <p>Ledgerwise can be adapted to your data warehouse on the cloud platform of your choice, using the strengths of each tool.</p>
      <p style="margin-top:3px">By combining our experience of systems integration with modern tools we design a setup that gives you the information you need, when you need it.</p>
      <p style="margin-top:3px;color:var(--ink)">– One of our special areas</p>
    </div>
    <div class="btn" style="left:41px;top:677px;width:59px">→ Read more about Studio</div>
    <div class="ph" role="img" aria-label="Photo of a team working together in an office" style="left:161px;top:602px;width:168px;height:86px;background:linear-gradient(120deg,#2b2a6e,#4a4f8c 50%,#1c1b55)">
      <div class="abs" style="left:12px;top:28px;width:110px;height:38px;background:rgba(240,242,248,.95);border-left:2px solid var(--green);padding:4px 5px">
        <p class="txt" style="color:var(--ink)">«Ledgerwise simplifies access to data and provides running KPIs, reports and in-depth analysis relating to our property portfolio, while also providing tools to support the business's overall financial reporting and planning activities.»</p>
        <p class="txt" style="margin-top:2px">Karen Solberg – Finance Director</p>
      </div>
    </div>
  </section>

  <!-- Perfect solution -->
  <section class="band band-glow" style="top:705px;height:95px">
    <h2 class="abs" style="left:41px;top:32px;font-size:9px;line-height:13px;font-weight:500;color:var(--white)">We develope the<br>perfect solution for you!</h2>
    <div class="ph" role="img" aria-label="Illustration of a person working with cloud data icons" style="left:180px;top:8px;width:80px;height:82px;background:radial-gradient(ellipse at 55% 45%,#3c8fe0 0%,#3130a0 45%,rgba(36,31,122,0) 75%)"></div>
  </section>

  <!-- Advanced analytics -->
  <section>
    <div class="ph circle-ph" role="img" aria-label="Tablet showing analytics charts" style="left:49px;top:815px;width:77px;height:80px"></div>
    <h2 class="abs h2" style="left:160px;top:816px">Advanced analytics</h2>
    <div class="abs txt" style="left:160px;top:830px;width:127px">
      <p>Advanced analytics are techniques that reveal patterns in your data, give you a view of what may happen next and help you act on it before it happens, not after.</p>
      <p style="margin-top:3px">With the right models and tools you can look beyond what happened and why it happened, and move toward clear forecasts you can trust.</p>
      <p style="margin-top:3px">Through the right choices you learn the options that work best, building models that serve your business and your data.</p>
      <p style="margin-top:3px;color:var(--ink)">– Predict the future</p>
    </div>
  </section>

  <!-- Cognis box -->
  <div class="box" style="left:0;top:913px;width:160px;height:82px">
    <h2 class="abs h2" style="left:41px;top:10px;font-size:6px">Cognis Intelligence Suite</h2>
    <div class="abs txt" style="left:41px;top:21px;width:107px">Cognis Intelligence Suite is an umbrella term for a range of cloud services and APIs provided by Northwind Cloud for building and presenting big data solutions. It gives you the tools to turn data into insight and action, with machine learning and clear dashboards in one place.</div>
    <p class="abs green" style="left:41px;top:66px;font-size:2.6px">– Everything at one place</p>
  </div>
  <ul class="checks" style="left:175px;top:943px">
    <li><i class="tick"></i>Increased customer satisfaction</li>
    <li><i class="tick"></i>Data-verified decisions</li>
    <li><i class="tick"></i>Increased productivity</li>
  </ul>

  <!-- Pulse BI -->
  <section>
    <h2 class="abs h2" style="left:41px;width:120px;top:1016px;text-align:right">Pulse BI</h2>
    <div class="abs txt" style="left:46px;top:1030px;width:115px;text-align:right">Pulse BI is a cloud analytics service from Northwind Cloud for building reports and dashboards. It brings data together from many sources so you get a complete view, shares results across the company and gives every user fast access to the figures that matter most, on any device.<br><span style="color:var(--ink)">– Your individual analytical tool</span></div>
    <div class="ph circle-ph" role="img" aria-label="Monitor showing a map and report dashboard" style="left:199px;top:1010px;width:77px;height:82px"></div>
  </section>

  <!-- Machine learning box -->
  <ul class="checks" style="left:60px;top:1137px;text-align:right">
    <li style="justify-content:flex-end">Improved precision of financial rules and models<i class="tick"></i></li>
    <li style="justify-content:flex-end">Increased efficiency<i class="tick"></i></li>
    <li style="justify-content:flex-end">Facilitating accurate predictions<i class="tick"></i></li>
  </ul>
  <div class="box" style="left:169px;top:1108px;width:160px;height:84px">
    <h2 class="abs h2" style="right:41px;top:9px;font-size:6px">Machinelearning</h2>
    <div class="abs txt" style="left:12px;top:21px;width:107px;text-align:right">Machine learning lets systems learn from data and improve over time. Models find patterns in your numbers, make forecasts and flag changes early, so your team can spend less time on manual checks and more time on the choices that move the business.</div>
    <p class="abs green" style="right:41px;top:66px;font-size:2.6px">– Analyze more and gain insight</p>
  </div>

  <!-- Related -->
  <section>
    <h2 class="abs" style="left:0;width:329px;top:1206px;text-align:center;font-size:6.5px;color:var(--ink)">Related solutions and services</h2>
    <div class="tile" style="left:79px;top:1228px"><svg width="12" height="10" viewBox="0 0 12 10"><path d="M3 8h6a2.5 2.5 0 0 0 0-5A3 3 0 0 0 3 4a2 2 0 0 0 0 4z" fill="none" stroke="#555" stroke-width=".7"/></svg><span>CLOUD</span></div>
    <div class="tile active" style="left:139px;top:1228px"><svg width="12" height="10" viewBox="0 0 12 10"><rect x="1" y="1" width="10" height="8" fill="none" stroke="#fff" stroke-width=".7"/><path d="M1 5h10M6 1v8" stroke="#fff" stroke-width=".5"/></svg><span>FINANCE AND PLANNING</span></div>
    <div class="tile" style="left:200px;top:1228px"><svg width="12" height="10" viewBox="0 0 12 10"><path d="M2 9V6M5 9V4M8 9V2M1 9.5h10" stroke="#555" stroke-width=".8"/></svg><span>REPORTING</span></div>
    <div class="tile" style="left:108px;top:1276px"><svg width="12" height="10" viewBox="0 0 12 10"><path d="M6 1L10 5L6 9L2 5Z" fill="none" stroke="#555" stroke-width=".7"/></svg><span>SOFTWARE</span></div>
    <div class="tile" style="left:168px;top:1276px"><svg width="12" height="10" viewBox="0 0 12 10"><circle cx="6" cy="5" r="3.5" fill="none" stroke="#555" stroke-width=".7"/><circle cx="6" cy="5" r="1" fill="#555"/></svg><span>SERVICES</span></div>
  </section>

  <!-- Contact -->
  <section class="band band-glow" style="top:1332px;height:88px">
    <svg class="abs" style="left:162px;top:13px" width="6" height="6" viewBox="0 0 10 10"><path d="M1 5L9 1L6 9L5 6Z" fill="var(--green)"/></svg>
    <h2 class="abs" style="left:0;width:329px;top:23px;text-align:center;font-size:6px;color:var(--white)">Contact us for more information</h2>
    <p class="abs green" style="left:0;width:329px;top:35px;text-align:center;font-size:3.2px">MATS LINDQVIST</p>
    <p class="abs" style="left:0;width:329px;top:49px;text-align:center;font-size:3.2px;color:var(--white)">Call: <span class="green">+47 400 12 345</span> &nbsp; Email: <span class="green">mats.lindqvist@ledgerwise-demo.com</span></p>
    <div class="btn" style="left:135px;top:64px;width:59px;height:9px;line-height:9px">Read more about us →</div>
  </section>

  <!-- Footer -->
  <footer class="band" style="top:1420px;height:80px;background:var(--navy-deep)">
    <div class="abs logo" style="left:0;width:329px;top:11px;text-align:center;font-size:6px">Ledgerwise</div>
    <p class="abs" style="left:0;width:329px;top:37px;text-align:center;font-size:2.6px;color:#c9c8e6"><span class="green">✆</span> +47 400 00 000 &nbsp; <span class="green">✉</span> post@ledgerwise-demo.com</p>
    <div class="abs" style="left:147px;top:50px;display:flex;gap:4px">
      <i style="width:5px;height:5px;border:.5px solid #6a6a9a;border-radius:50%"></i><i style="width:5px;height:5px;border:.5px solid #6a6a9a;border-radius:50%"></i><i style="width:5px;height:5px;border:.5px solid #6a6a9a;border-radius:50%"></i><i style="width:5px;height:5px;border:.5px solid #6a6a9a;border-radius:50%"></i>
    </div>
    <p class="abs" style="left:41px;top:71px;font-size:2.2px;color:#7a7aa0">Copyright © 2019 Ledgerwise AS all rights reserved</p>
    <svg class="abs" style="left:284px;top:71px" width="4" height="3" viewBox="0 0 4 3"><path d="M.5 2.5L2 1L3.5 2.5" fill="none" stroke="#7a7aa0" stroke-width=".5"/></svg>
  </footer>

</main>
</body>
</html>
```